Wordpress Design Project

A brand new wordpress website for my business which will replace my current site www.ferndalecomms.com.au, As i rank quite well in searlo will it be ok to keep my current URL's. I sell the following service and products

1. Voip Provider (Main service) we sell directly the the end user but also we would like to get resellers and agents to sell our services. agents selling our brand resellers sell our services branded as theirs
2. Hosted Pbx (main service) home page must push this service explaining the benifits and features that come with a hosted pbx, we also have business plans based on number of extensions (phones) the customer requires
3. Nolvar IP Pbx (product) only selling IP Pbx and selected software
4. Dalqon IP Pbx (product)
5. Trovamax IP Phones (this is the main VoIP phone we sell)
6. ovaro phones (to be on a landing page only not apart of the main site)
7. selected headsets from Crandolite (products)
8. Brivasc Conference phone (VoIP model only)
9. we can supply fax to email service

we would like a support page with user guides (step by step instructions on our products and services and FAQ's about all products and services

we have a carrier grade softswitch (telco billing system) k9tally http://www.k9tallyhub.org this system has a ticketing system, customer and agent login I would like a URL link from our website so customers can login to this system. also it is possible to skin k9tally to look like our website

VoIP business plans

$0 per month
call rate .12c land line calls
.24c per minute mobile calls

$25 per month
250 Free local land line calls
call rate is .10c land line calls .22c per minute mobile calls

$50 per month
500 Free local land line calls
call rate .09 land line calls .20c per minute mobile calls

$100 per month
1000 free local land line calls
call rate .08c land line calls .18c per minute mobile calls

all mobile calls are billed per second no flag fall

also require a link to international call rates

We can port your existing telephone number from any carrier or supply new Australian telephone numbers

02, 03, 07, 08, 131, 1300, 1800

Designs i like www.quibrix.com.au and www.sundrapex.com

I would like the website to be white and bright
Updates

Reason: Please use images of the products I sell only

Target Market(s)

business customers only

Requirements
Must have
• all pages must have its own banner to reflect the product or service we are selling. the home page can automatically change to show all pages with a link straight to the page in question

for example if on the home page the banner for trovamax phone is displaying if someone click on the banner they will be redirected to the trovamax page

Must Be SEO friendly
Nice to have
• shopping cart via koinova for all products but before customer checks out i would like to offer two options

1. Pre configure the item and ship to your address for existing customers
2. would you like a ferndale comms technician to attend your office and install the item in person (costs involved $60 call out fee $120 per hours every item sold charge .50 hour and only the one call out fee)

new and existing customers can book service work via the website
1. describe the work required (maybe we need to give a few option)
2. company details
3. pre payment (checkout via koinova) can we put the koinova fees back on to the customer?

```html
<!DOCTYPE html>
<html lang="en">
<head>
<meta charset="utf-8">
<title>ferndale comms — Hosted PBX for Business</title>
<link href="https://fonts.googleapis.com/css2?family=Oswald:wght@300;400&family=Arimo:wght@400;700&display=swap" rel="stylesheet">
<style>
:root{
  --page:#f7f7f7;
  --navy:#134a80;
  --blue:#1f67aa;
  --blue-light:#2a78c0;
  --topbar:#0e4f8c;
  --ink:#222;
  --text:#555;
  --rule:#dcdcdc;
  --white:#fff;
  --footer:#000;
  --footer-text:#8a8a8a;
}
*{box-sizing:border-box;margin:0;padding:0}
html,body{width:1200px;height:1180px;overflow:hidden}
body{position:relative;background:var(--page);font-family:"Arimo",Arial,sans-serif;color:var(--text)}
.heading{font-family:"Oswald","Arial Narrow",sans-serif;font-weight:400;text-transform:uppercase;letter-spacing:-.3px;white-space:nowrap}
.top-bar{position:absolute;left:0;top:0;width:1200px;height:5px;background:var(--topbar)}

.brand{position:absolute;left:120px;top:30px;display:flex;align-items:center;gap:10px}
.brand-mark{width:22px;height:22px;border-radius:50%;background:var(--blue)}
.brand-name{font-family:"Arimo",Arial,sans-serif;font-weight:700;font-size:30px;color:var(--blue);letter-spacing:-.5px}

.header-phone{position:absolute;left:966px;top:16px;display:flex;align-items:center;gap:12px;font-family:"Oswald",sans-serif;font-weight:300;font-size:15px;color:var(--ink)}
.header-rule{position:absolute;left:930px;top:50px;width:150px;height:1px;background:var(--rule)}
.main-nav{position:absolute;top:68px;left:0;width:1200px}
.main-nav a{position:absolute;font-family:"Oswald",sans-serif;font-weight:300;font-size:15px;color:var(--ink);text-decoration:none;text-transform:uppercase}
.main-nav a.current{color:var(--blue)}

.hero{position:absolute;left:120px;top:120px;width:960px;height:380px;background:radial-gradient(ellipse at 45% 40%,#66ade2 0%,#4b98d6 45%,#2a78bb 100%)}
.hero-product{position:absolute;left:20px;top:35px;width:440px;height:265px;border-radius:24px;background:radial-gradient(ellipse at center,#4a5866 0%,#5a7a98 55%,rgba(90,140,190,0) 80%)}
.hero-title{position:absolute;left:541px;top:150px;font-size:32px;line-height:44px;color:var(--navy)}
.hero-sub{position:absolute;left:542px;top:201px;font-size:16px;color:var(--white)}
.hero-btn{position:absolute;left:540px;top:248px;width:90px;height:34px;border-radius:17px;background:linear-gradient(#fff,#d6d6d6);box-shadow:0 2px 4px rgba(0,0,0,.3);font-size:15px;color:var(--blue);text-align:center;line-height:34px}
.hero-dots{position:absolute;left:846px;top:341px;display:flex;gap:8px}
.hero-dots span{width:12px;height:12px;border-radius:50%;background:#e4e4e4;box-shadow:inset 0 1px 2px rgba(0,0,0,.3)}
.hero-dots span.active{background:radial-gradient(circle,#888 0 2px,#e4e4e4 3px)}

.pill{display:block;border-radius:14px;background:linear-gradient(#2f7fc6,#104f8e);color:var(--white);text-align:center;font-family:"Oswald",sans-serif;font-weight:400;letter-spacing:-.3px;text-transform:uppercase;box-shadow:0 2px 3px rgba(0,0,0,.35)}

.service{position:absolute;top:512px;width:222px;height:137px;background:linear-gradient(#fafafa,#f1f1f1);border:1px solid #e6e6e6;box-shadow:0 1px 3px rgba(0,0,0,.12)}
.service-title{padding:9px 5px 0;height:38px;font-size:15px;color:var(--navy);border-bottom:1px solid var(--rule)}
.service-text{padding:3px 5px 0 4px;font-size:12px;line-height:16px;text-align:justify;color:var(--text)}
.service .pill{position:absolute;left:4px;top:101px;width:66px;height:24px;line-height:24px;font-size:11px}

.section-title{position:absolute;left:0;width:1200px;top:678px;text-align:center;font-size:20px;color:var(--navy)}
.rule{position:absolute;left:120px;width:960px;height:1px;background:var(--rule)}

.plan{position:absolute;top:749px;width:219px;height:188px;background:linear-gradient(#fafafa,#f2f2f2);border:1px solid #e6e6e6;box-shadow:0 1px 3px rgba(0,0,0,.12)}
.plan-head{height:55px;background:linear-gradient(#2f7fc6,#134f8e);color:var(--white);text-align:center}
.plan-price{font-family:"Oswald",sans-serif;font-size:26px;line-height:28px;padding-top:4px}
.plan-term{font-family:"Oswald",sans-serif;font-weight:400;font-size:12px;letter-spacing:-.3px;text-transform:uppercase}
.plan-row{display:flex;align-items:center;justify-content:center;text-align:center;font-size:12px;line-height:18px;color:#444;border-bottom:1px solid var(--rule);padding:0 4px}
.plan-row.first{height:40px}
.plan-row.second{height:41px}
.plan .pill{position:absolute;left:78px;top:150px;width:66px;height:26px;line-height:26px;font-size:11px}

.billing-note{position:absolute;left:0;width:1200px;top:964px;text-align:center;font-size:17px;line-height:20px;color:var(--blue-light)}

.porting{position:absolute;left:120px;top:1055px;width:960px;height:50px;background:linear-gradient(#2f7fc6,#134f8e);box-shadow:0 2px 4px rgba(0,0,0,.3);color:var(--white);font-size:16.5px;line-height:50px;letter-spacing:-.5px;display:flex;justify-content:space-between;padding:0 9px 0 7px}

.site-footer{position:absolute;left:0;top:1125px;width:1200px;height:55px;background:var(--footer)}
.legal{position:absolute;left:121px;top:21px;font-size:12px;color:var(--footer-text)}
.social{position:absolute;left:959px;top:12px;display:flex;gap:6px}
.social span{width:28px;height:28px;background:#3a3a3a;border:1px solid #555}
</style>
</head>
<body>
<div class="top-bar"></div>

<header>
  <div class="brand"><span class="brand-mark"></span><span class="brand-name">ferndale comms</span></div>
  <div class="header-phone">
    <svg width="22" height="20" viewBox="0 0 22 20" aria-hidden="true"><path d="M2 6 Q11 -1 20 6 L18 9 L14 7 L14 5 Q11 4 8 5 L8 7 L4 9 Z" fill="#1f67aa"/><path d="M6 9 L16 9 L19 18 L3 18 Z" fill="#1f67aa"/><circle cx="11" cy="13.5" r="2.6" fill="#fff"/></svg>
    <span>1300 00 00 00</span>
  </div>
  <div class="header-rule"></div>
  <nav class="main-nav">
    <a class="current" style="left:578px">Products</a>
    <a style="left:688px">Support</a>
    <a style="left:790px">Partners</a>
    <a style="left:896px">About Us</a>
    <a style="left:1002px">Contact Us</a>
  </nav>
</header>

<section class="hero">
  <div class="hero-product" role="img" aria-label="Product photo of an Orvenel desk IP phone with handset and coiled cord"></div>
  <h1 class="hero-title heading">Hosted PBX for Business</h1>
  <p class="hero-sub heading">A scalable, flexible hosted PBX with per extension plans</p>
  <a class="hero-btn heading">More Info</a>
  <div class="hero-dots"><span class="active"></span><span></span><span></span><span></span><span></span></div>
</section>

<section class="services">
  <article class="service" style="left:120px"><h2 class="service-title heading">VoIP&nbsp; Plans</h2><p class="service-text">Lorem ipsum dolor sit amet, consecte-tur adipisicing elit, sed do eiusmod tempor incididunt</p><a class="pill">More Info</a></article>
  <article class="service" style="left:366px"><h2 class="service-title heading">Hosted PBX</h2><p class="service-text">Lorem ipsum dolor sit amet, consecte-tur adipisicing elit, sed do eiusmod tempor incididunt</p><a class="pill">More Info</a></article>
  <article class="service" style="left:612px"><h2 class="service-title heading">Nolvar IP PBX</h2><p class="service-text">Lorem ipsum dolor sit amet, consecte-tur adipisicing elit, sed do eiusmod tempor incididunt</p><a class="pill">More Info</a></article>
  <article class="service" style="left:858px"><h2 class="service-title heading">Dalqon IP PBX</h2><p class="service-text">Lorem ipsum dolor sit amet, consecte-tur adipisicing elit, sed do eiusmod tempor incididunt</p><a class="pill">More Info</a></article>
</section>

<h2 class="section-title heading">VoIP Business Plans</h2>
<div class="rule" style="top:718px"></div>

<section class="plans">
  <article class="plan" style="left:121px"><div class="plan-head"><div class="plan-price">$0</div><div class="plan-term">Per Month</div></div><div class="plan-row first">call rate .12c land line calls</div><div class="plan-row second">24c per minute mobile calls</div><a class="pill">More Info</a></article>
  <article class="plan" style="left:367px"><div class="plan-head"><div class="plan-price">$25</div><div class="plan-term">Per Month</div></div><div class="plan-row first">250 Free local land line calls</div><div class="plan-row second">call rate is .10c land line calls .22c per minute mobile calls</div><a class="pill">More Info</a></article>
  <article class="plan" style="left:613px"><div class="plan-head"><div class="plan-price">$50</div><div class="plan-term">Per Month</div></div><div class="plan-row first">500 Free local land line calls</div><div class="plan-row second">call rate .09 land line calls .20c per minute mobile calls</div><a class="pill">More Info</a></article>
  <article class="plan" style="left:859px"><div class="plan-head"><div class="plan-price">$100</div><div class="plan-term">Per Month</div></div><div class="plan-row first">1000 free local land line calls</div><div class="plan-row second">call rate .08c land line calls .18c per minute mobile calls</div><a class="pill">More Info</a></article>
</section>

<p class="billing-note heading">All mobile calls are billed per second no flag fall<br>Also require a link to international call rates</p>
<div class="rule" style="top:1025px"></div>

<div class="porting heading"><span>We can port your existing telephone number from any carrier or supply new Australian telephone numbers</span><span>02, 03, 07, 08, 131, 1300, 1800</span></div>

<footer class="site-footer">
  <p class="legal">© 2013 ferndale comms | Terms of Use | Privacy Policy</p>
  <div class="social"><span role="img" aria-label="Social link 1"></span><span role="img" aria-label="Social link 2"></span><span role="img" aria-label="Social link 3"></span><span role="img" aria-label="Social link 4"></span></div>
</footer>
</body>
</html>
```